Crestline 14 Industrial Park Needs Website

We are looking for a website for a new project we are working on.
Project does not have a logo so just use text. Needs to be responsive and mobile friendly for all browsers and coded for both Android & IOS. SEO is also important. Want something visually grabbing that displays growth, quality and confidence.
WordPress or Joomla – must be desktop and mobile friendly with fast page load speed. Need the ability to edit ourselves.
See attached website brief for further information.
Land Sale/Lease/Development
Coded - Design and coding required
4 page

```html
<!DOCTYPE html>
<html lang="en">
<head>
<meta charset="utf-8">
<title>Crestline 14 Industrial Park</title>
<link href="https://fonts.googleapis.com/css2?family=Cormorant+Garamond:wght@500;600&family=Libre+Baskerville&family=Lato:wght@300;400&display=swap" rel="stylesheet">
<style>
:root{
  --blue:#0b50b3;
  --blue-deep:#083f94;
  --blue-bar:#1c63d6;
  --accent:#6b9fd8;
  --accent-soft:#a9c6ea;
  --pale:#e6eef8;
  --ink:#3b4350;
  --white:#ffffff;
}
*{margin:0;padding:0;box-sizing:border-box}
html,body{width:1200px;height:4027px;overflow:hidden}
body{position:relative;background:var(--white);font-family:"Libre Baskerville",Georgia,serif;color:var(--ink)}
.abs{position:absolute}
.heading{font-family:"Cormorant Garamond",Georgia,serif;font-weight:600;text-transform:uppercase;letter-spacing:1px;color:var(--accent);line-height:1.05}
.body-text{font-size:12px;line-height:16.5px;color:var(--ink)}
.photo{position:absolute;border:2px solid #dfe8f3}

/* header */
.hero{left:0;top:0;width:1200px;height:612px;background:linear-gradient(180deg,#1c1f22 0%,#3b4240 18%,#59665c 45%,#6f7870 70%,#8a8f8c 100%)}
.brand{left:44px;top:22px;display:flex;align-items:center;gap:10px;color:var(--white);font-family:"Cormorant Garamond",serif;font-weight:600}
.brand-mark{width:34px;height:34px;background:var(--white)}
.brand-name{font-size:21px;line-height:20px}
.brand-name small{display:block;font-size:12px;line-height:14px}
.nav{left:725px;top:34px;display:flex;gap:0;font-size:11px;color:var(--white)}
.nav a{color:var(--white);text-decoration:none;position:absolute;white-space:nowrap}
.nav a.active{text-decoration:underline}
.btn-inquiry{left:1040px;top:27px;width:116px;height:32px;background:#8cb6e8;border:2px solid #dfe9f6;color:var(--blue-deep);font-size:10px;display:flex;align-items:center;justify-content:center;letter-spacing:.5px}

/* intro */
.intro-photo{left:156px;top:534px;width:388px;height:486px;background:linear-gradient(160deg,#9fc7ef 0%,#b98a5a 45%,#6e6a66 80%,#a58e79 100%)}
.intro-title{left:612px;top:683px;width:420px;font-size:32px}
.intro-text{left:612px;top:828px;width:437px}
.btn-outline{left:612px;top:931px;width:122px;height:33px;border:2px solid #c9d6e6;font-size:9.5px;display:flex;align-items:center;justify-content:center;color:var(--ink)}

/* why */
.why{left:0;top:1102px;width:1200px;height:648px;background:linear-gradient(125deg,#0a49a8 0%,#0d56bd 45%,#0a4cae 70%,#0f5cc4 100%)}
.why-title{left:156px;top:1170px;font-size:30px;color:var(--white)}
.why-sub{left:156px;top:1204px;font-size:24px;color:var(--accent-soft)}
.feature{top:1262px;display:flex;gap:10px;align-items:center;color:var(--white);font-size:12.5px;line-height:14px}
.feature-icon{width:50px;height:50px;background:rgba(255,255,255,.12);border:1px solid rgba(255,255,255,.35);display:flex;align-items:center;justify-content:center}
.why-text{left:706px;top:1170px;width:352px;color:#e4edf9}
.rule{left:156px;top:1386px;width:906px;height:1px;background:rgba(255,255,255,.2)}
.projects-title{left:300px;top:1454px;width:600px;text-align:center;font-size:32px;color:var(--white)}
.arrow{top:1634px}
.card{top:1553px;width:232px;height:245px;border:2px solid #5f8fd6;display:flex;align-items:flex-end;justify-content:center;padding-bottom:10px;color:var(--white);font-family:"Cormorant Garamond",serif;font-weight:600;font-size:14px;text-align:center;line-height:16px;text-transform:uppercase}

/* developments */
.dev{left:0;top:1750px;width:1200px;height:1430px;background:var(--pale)}
.dev-title{left:300px;top:1870px;width:600px;text-align:center;font-size:32px}
.tab{top:1975px;display:flex;gap:10px;align-items:center;font-size:13px;color:var(--accent);line-height:14px}
.tab-num{width:44px;height:44px;background:#b3cdec;color:var(--white);font-family:"Cormorant Garamond",serif;font-size:22px;display:flex;align-items:center;justify-content:center}
.block-title{font-size:23px}
</style>
</head>
<body>

<!-- header / hero -->
<div class="abs hero" role="img" aria-label="Aerial photograph of an office and industrial park with trees and parking lots"></div>
<div class="abs brand"><span class="brand-mark"></span><span class="brand-name">CRESTLINE 14<small>Industrial Park</small></span></div>
<nav class="abs nav">
  <a class="active" style="left:0">Home</a>
  <a style="left:56px">Why St.Paul</a>
  <a style="left:147px">Lot Layout</a>
  <a style="left:230px">Contact</a>
</nav>
<div class="abs btn-inquiry">INQUIRY NOW</div>

<!-- intro -->
<div class="photo intro-photo" role="img" aria-label="Photograph of a modern glass apartment tower at sunset"></div>
<h1 class="abs heading intro-title">The property is located on the west side of the town of St. Paul</h1>
<p class="abs body-text intro-text">a growing municipality located northeast of Edmonton, with a regional population of 13,649. The area has a very strong local economy due to its location between Edmonton and Cold Lake, but with a stronger agricultural base. It serves as the focal point for the Smoky Lake area, with an unemployment rate of 5.0% lower than the provincial average of 8.2%.</p>
<div class="abs btn-outline">LEARN MORE</div>

<!-- why st paul -->
<section class="abs why"></section>
<h2 class="abs heading why-title">Why St Paul?</h2>
<div class="abs heading why-sub">Location Advantage</div>
<div class="abs feature" style="left:156px">
  <span class="feature-icon"><svg width="26" height="26" viewBox="0 0 24 24" fill="none" stroke="#fff" stroke-width="1.5"><path d="M12 22s7-7 7-12a7 7 0 0 0-14 0c0 5 7 12 7 12z"/><circle cx="12" cy="10" r="2.5"/></svg></span>
  <span>Prime<br>location to<br>service</span>
</div>
<div class="abs feature" style="left:331px">
  <span class="feature-icon"><svg width="28" height="26" viewBox="0 0 24 24" fill="none" stroke="#fff" stroke-width="1.5"><path d="M3 11l9-7 9 7"/><path d="M5 10v10h14V10"/><path d="M9 17l6-6"/><circle cx="9.5" cy="12" r="1"/><circle cx="14.5" cy="16" r="1"/></svg></span>
  <span>Lower<br>property<br>tax</span>
</div>
<div class="abs feature" style="left:488px">
  <span class="feature-icon"><svg width="26" height="26" viewBox="0 0 24 24" fill="none" stroke="#fff" stroke-width="1.5"><rect x="4" y="6" width="8" height="15"/><rect x="12" y="2" width="8" height="19"/><path d="M6.5 9h3M6.5 12h3M6.5 15h3M14.5 6h3M14.5 9h3M14.5 12h3M14.5 15h3"/></svg></span>
  <span>Better visibility<br>for highway<br>commercial</span>
</div>
<p class="abs body-text why-text">Located in the County of St. Paul business area, which is currently short of product for sale or lease in both residential and commercial real estate. The area is also in a current influx of population due to its close proximity to the development occurring in the Industrial Heartland. The County of St. Paul is a designated community under the Rural Renewal Stream (RRS) of the provincial Advantage Immigration Program.</p>
<div class="abs rule"></div>
<h2 class="abs heading projects-title">Major projects in St. Paul service area</h2>
<svg class="abs arrow" style="left:196px" width="20" height="30" viewBox="0 0 20 30" fill="none" stroke="#a9c6ea" stroke-width="2"><path d="M15 3L4 15l11 12"/></svg>
<svg class="abs arrow" style="left:232px;top:1672px" width="20" height="30" viewBox="0 0 20 30" fill="none" stroke="#a9c6ea" stroke-width="2"><path d="M5 3l11 12L5 27"/></svg>
<div class="abs card" style="left:311px;background:linear-gradient(180deg,#d9d2c6,#9c8a75 70%,#3b3530)" role="img" aria-label="Photograph of a modern residential building with balconies">Birchwood Solar<br>Project</div>
<div class="abs card" style="left:561px;background:linear-gradient(180deg,#8db4dc,#5e7e4f 55%,#2c3a2c)" role="img" aria-label="Photograph of a tower covered in green plants">Prairie Crest<br>Wind Project</div>
<div class="abs card" style="left:811px;background:linear-gradient(180deg,#3e4a8c,#8a5a2e 45%,#c9a15c 70%,#2a2420)" role="img" aria-label="Photograph of a lit glass and timber office building at dusk">North Base<br>Expansion</div>
<div class="abs card" style="left:1061px;width:150px;background:linear-gradient(180deg,#c6d8ea,#6a8298 60%,#2e3a46)" role="img" aria-label="Photograph of city towers">Birchwood Sol<br>Project</div>

<!-- recent developments -->
<section class="abs dev"></section>
<h2 class="abs heading dev-title">Recent commercial developments or expansions</h2>
<div class="abs tab" style="left:317px"><span class="tab-num">01</span>Fieldway</div>
<div class="abs tab" style="left:506px"><span class="tab-num">02</span>Marchand &amp; Sons<br>Implements Ltd</div>
<div class="abs tab" style="left:727px"><span class="tab-num">03</span>Ridgeline<br>Heavy Equipment</div>

<div class="photo" style="left:156px;top:2062px;width:388px;height:321px;background:linear-gradient(135deg,#f3f3f1 0%,#2f5b8a 35%,#1f4a7a 60%,#e8e6e2 80%,#d9742e 100%)" role="img" aria-label="Photograph of a tablet showing a floor plan with rulers and pencils"></div>
<h3 class="abs heading block-title" style="left:609px;top:2142px">Development plans</h3>
<p class="abs body-text" style="left:611px;top:2176px;width:400px">It is currently anticipated that the process of sub-dividing the property and installing the required services to allow for sub-division will take 18 months to complete. The developer is proposing to develop the industrial park to include a truck/RV service centre including a restaurant, a truck/RV car wash and three buildings with 6 bays of office warehouse condos averaging 2,400 square feet per bay. These units will be offered for sale or lease. Presently there is no available space of this nature in the area.</p>

<h3 class="abs heading block-title" style="left:156px;top:2484px">Industrial<br>condominium complex</h3>
<p class="abs body-text" style="left:156px;top:2546px;width:440px">Upon re-zoning and sub-division, the project will move forward with construction on as many as three industrial office warehouses. Each of these buildings will consist of a building footprint of roughly 14,500 SF and 6 individually titled units as part of a condo complex. Each building will be situated with highway frontage to maximize exposure, and yard space in the rear. The developer has found this to be the ideal product for small to medium-sized businesses, which is currently lacking in the St Paul market. They have built a similar project in Sherwood Park, known as The Maplestone Business Condominiums.</p>
<div class="photo" style="left:656px;top:2416px;width:388px;height:318px;background:linear-gradient(180deg,#2f7ad6 0%,#7fb2e6 40%,#6c8a56 65%,#e6e6e2 100%)" role="img" aria-label="Photograph of a white building with green terraces"></div>

<div class="photo" style="left:156px;top:2781px;width:388px;height:321px;background:linear-gradient(180deg,#3d7fd0 0%,#bcd6ee 40%,#9aa2a8 65%,#8a8c8c 100%)" role="img" aria-label="Photograph of a large industrial shop with a loading canopy"></div>
<h3 class="abs heading block-title" style="left:609px;top:2864px">Existing shop</h3>
<p class="abs body-text" style="left:611px;top:2898px;width:395px">The existing shop will be parcelled together with a storage yard and sold as is. This will allow for the shop to be purchased or leased along with 2-3 acres of gravelled and fenced yard space.<br>Upon sub-division, the developers intend to sell this property for an estimated price of $1,400,000. This property is presently being leased and a Letter of Intent to purchase has been agreed to by the existing tenant.</p>

<!-- lot layout -->
<h2 class="abs heading" style="left:300px;top:3247px;width:600px;text-align:center;font-size:25px">Appraisal lot layout</h2>
<p class="abs body-text" style="left:236px;top:3285px;width:728px;text-align:center">This Area Structure Plan is preliminary and will require modification. Provincial Transportation is considering our proposal for access to the property off Range Road 100 to alleviate significant costs related to access from Highway 29.</p>

<!-- footer -->
<footer class="abs" style="left:0;top:3648px;width:1200px;height:346px;background:var(--blue)"></footer>
<div class="abs" style="left:156px;top:3341px;width:888px;height:365px;border:2px solid #7fa9e0;background:var(--white);padding:5px">
  <div style="width:100%;height:100%;background:linear-gradient(135deg,#6e6656 0%,#8a8270 35%,#7a8a86 55%,#9ab0c0 65%,#7f7866 85%,#6a6454 100%)" role="img" aria-label="Aerial site map with numbered lots, truck stop and stormwater facility"></div>
</div>
<div class="abs brand" style="left:472px;top:3774px;gap:10px"><span class="brand-mark" style="width:40px;height:40px"></span><span class="brand-name" style="font-size:25px;line-height:24px">CRESTLINE 14<small style="font-size:16px;line-height:18px">Industrial Park</small></span></div>
<div class="abs" style="left:0;top:3862px;width:1200px;display:flex;justify-content:center;align-items:center;gap:26px;font-family:'Lato',sans-serif;font-weight:300;font-size:28px;color:var(--accent-soft)">
  <span>+112 555 014</span><span style="width:1px;height:32px;background:rgba(255,255,255,.3)"></span><span>info@crestline14.com</span>
</div>
<div class="abs" style="left:0;top:3924px;width:1200px;display:flex;justify-content:center;gap:32px;font-size:11px;color:var(--white)">
  <span style="text-decoration:underline">Home</span><span>Why St.Paul</span><span>Lot Layout</span><span>Contact</span>
</div>
<div class="abs" style="left:0;top:3994px;width:1200px;height:33px;background:var(--blue-bar)"></div>
<div class="abs" style="left:46px;top:4004px;font-size:9.5px;color:var(--white)">© 2024 Crestline 14. All Right Reserved</div>
<div class="abs" style="left:1054px;top:4000px;display:flex;gap:7px">
  <span style="width:19px;height:19px;border-radius:50%;background:#a9c6ea"></span>
  <span style="width:19px;height:19px;border-radius:50%;background:#a9c6ea"></span>
  <span style="width:19px;height:19px;border-radius:50%;background:#a9c6ea"></span>
  <span style="width:19px;height:19px;border-radius:50%;background:#a9c6ea"></span>
</div>

</body>
</html>
```